Tri-Fold Brochure – Mobility, Family & Pet Rentals

I need a clean, premium tri-fold brochure (A4 unfolded) for hotel guests in Madrid. It should present our rental services and make it very easy to contact us via QR code or WhatsApp.

The design must visually match the style of our websites:
• wheelvale.es (mobility scooters)
• kitbrook.es (baby, family, pet equipment)

The brochure should feel consistent with these brands.

⸻

Style
• Must reflect the look & feel of our websites (very important)
• Clean, modern, friendly
• Not medical
• Tourist-focused, lifestyle
• Simple, convenient, trustworthy

⸻

Key messages to highlight
• Free delivery & pickup at hotels in central Madrid
• No deposit required
• Guests can leave equipment at hotel → we collect it
• Easy booking via WhatsApp
• High-quality, modern equipment

⸻

Content (6 panels)

1. Front cover
• “Mobility, Family & Pet Rentals in Madrid”
• “Delivered directly to your hotel”
• Lifestyle image (Madrid + scooter)

2. Inside – Mobility
• Show mobility scooters
• Lightweight, easy to use, ideal for sightseeing

3. Inside – Why choose us
• Free delivery & pickup at hotel
• No deposit
• Fast, reliable service
• Clean, ready-to-use equipment

4. Inside – Other rentals (Kitbrook)
• Baby: cribs, strollers
• Family travel equipment
• Pets: strollers, carriers
• Mention kitbrook.es (secondary)

5. Contact / CTA
• Large QR code (very visible)
• WhatsApp number (prominent)
• Website: wheelvale.es

6. How it works
• Contact us (QR / WhatsApp)
• We deliver to your hotel
• Use it and leave it at reception

⸻

Requirements
• Keep text minimal
• Clear hierarchy
• QR code must be large and easy to scan

⸻

Deliverables
• Print-ready (CMYK, bleed)
• Digital PDF (for sharing)

```html
<!DOCTYPE html>
<html lang="en">
<head>
<meta charset="utf-8">
<title>Rentals Brochure – Inside Spread</title>
<link rel="stylesheet" href="https://fonts.googleapis.com/css2?family=Poppins:wght@300;400;600;700&display=swap">
<style>
  :root {
    --red: #c1202a;
    --yellow: #f9c013;
    --ink: #111111;
    --body: #3a3a3a;
    --white: #ffffff;
  }
  * { margin: 0; padding: 0; box-sizing: border-box; }
  html, body { width: 1200px; height: 927px; overflow: hidden; background: var(--white); }
  body { font-family: "Poppins", sans-serif; position: relative; }

  .panel { position: absolute; top: 0; width: 400px; height: 927px; overflow: hidden; }
  .panel--rentals { left: 0; }
  .panel--why { left: 400px; }
  .panel--mobility { left: 800px; }

  .media { position: absolute; }

  /* Left panel */
  .rentals__band { position: absolute; left: 0; top: 0; width: 400px; height: 319px; background: var(--yellow); border-radius: 0 0 70px 70px; }
  .rentals__photo { left: 0; top: 0; width: 400px; height: 279px; border-radius: 0 0 70px 70px;
    background: linear-gradient(160deg, #5f8a3a 0%, #8db35a 45%, #c9b9a3 75%, #a9a29a 100%); }
  .section-title { position: absolute; font-weight: 700; font-size: 28px; color: var(--ink); line-height: 1; white-space: nowrap; }
  .section-title .light { font-weight: 400; }
  .rule { position: absolute; height: 5px; width: 69px; background: var(--yellow); }
  .bullets { position: absolute; list-style: none; color: var(--red); font-weight: 600; font-size: 19px; line-height: 1; white-space: nowrap; }
  .bullets li::before { content: "•"; margin-right: 8px; }
  .rentals__title { left: 28px; top: 338px; }
  .rentals__rule { left: 29px; top: 376px; }
  .rentals__list { left: 42px; top: 406px; }
  .rentals__list li { margin-bottom: 11px; }
  .pet-photo { left: 55px; top: 522px; width: 270px; height: 335px; border-radius: 18px;
    background: radial-gradient(ellipse at 55% 55%, #d8ccb2 0%, #c2b391 50%, #f4f1ea 85%); }
  .rentals__footer { position: absolute; left: 0; top: 800px; width: 400px; height: 100px; background: var(--red); border-radius: 0 0 70px 70px; }
  .rentals__footer-cap { position: absolute; left: 0; top: 780px; width: 400px; height: 80px; background: var(--white); border-radius: 0 0 70px 70px; }
  .site-link { position: absolute; left: 128px; top: 866px; color: var(--white); font-size: 18px; font-weight: 400; display: flex; align-items: center; gap: 6px; }
  .site-link svg { width: 17px; height: 17px; }
  .site-tag { position: absolute; left: 291px; top: 871px; color: var(--yellow); font-size: 12px; }

  /* Middle panel */
  .why__photo { left: 0; top: 590px; width: 400px; height: 337px;
    background: linear-gradient(180deg, #e9e4da 0%, #cfc7b9 40%, #8e8a84 75%, #5b5853 100%); }
  .why__band { position: absolute; left: 0; top: 0; width: 400px; height: 647px; background: var(--yellow); border-radius: 0 0 70px 70px; }
  .why__card { position: absolute; left: 0; top: 0; width: 400px; height: 610px; background: var(--red); border-radius: 0 0 70px 70px; overflow: hidden; }
  .why__cut { position: absolute; left: 0; top: 0; }
  .brand-name { position: absolute; left: 0; width: 400px; top: 196px; display: flex; justify-content: center; align-items: center; gap: 12px;
    color: var(--white); font-weight: 700; font-size: 44px; line-height: 1; }
  .brand-name .dot { width: 26px; height: 26px; border-radius: 50%; background: var(--yellow); }
  .why__title { position: absolute; left: 28px; top: 368px; color: var(--white); font-weight: 700; font-size: 27px; line-height: 1; }
  .why__list { left: 42px; top: 428px; color: var(--white); }
  .why__list li { margin-bottom: 17px; }

  /* Right panel */
  .mobility__band { position: absolute; left: 0; top: 30px; width: 400px; height: 200px; background: var(--yellow); border-radius: 55px 55px 0 0; }
  .mobility__sheet { position: absolute; left: 0; top: 81px; width: 400px; height: 846px; background: var(--white); border-radius: 55px 55px 0 0; }
  .scooter-photo { left: 13px; top: 85px; width: 370px; height: 388px; border-radius: 20px;
    background: radial-gradient(ellipse at 55% 55%, #4a4a4c 0%, #7a7a7d 40%, #f2f2f2 80%); }
  .mobility__title { left: 27px; top: 517px; }
  .mobility__rule { left: 27px; top: 555px; }
  .mobility__list { left: 42px; top: 585px; }
  .mobility__list li { margin-bottom: 11px; }
  .mobility__copy { position: absolute; left: 27px; top: 692px; width: 350px; font-size: 14.3px; font-weight: 300; line-height: 22.8px; color: var(--body); }
</style>
</head>
<body>

<section class="panel panel--rentals">
  <div class="rentals__band"></div>
  <div class="media rentals__photo" role="img" aria-label="Father walking in a park with a toddler and a grey baby stroller"></div>
  <h2 class="section-title rentals__title">Other Rentals <span class="light">(Kitbrook)</span></h2>
  <div class="rule rentals__rule"></div>
  <ul class="bullets rentals__list">
    <li>Baby: cribs, strollers</li>
    <li>Family travel equipment</li>
    <li>Pets: strollers, carriers</li>
  </ul>
  <div class="rentals__footer"></div>
  <div class="rentals__footer-cap"></div>
  <div class="media pet-photo" role="img" aria-label="Small white dog sitting in a beige pet stroller"></div>
  <div class="site-link">
    <svg viewBox="0 0 24 24" fill="none" stroke="#fff" stroke-width="2"><circle cx="12" cy="12" r="10"/><path d="M2 12h20M12 2c3 3 4 6.5 4 10s-1 7-4 10M12 2c-3 3-4 6.5-4 10s1 7 4 10"/></svg>
    kitbrook.es
  </div>
  <div class="site-tag">(secondary)</div>
</section>

<section class="panel panel--why">
  <div class="media why__photo" role="img" aria-label="Bear and strawberry tree statue in central Madrid"></div>
  <div class="why__band"></div>
  <div class="why__card">
    <svg class="why__cut" width="400" height="220" viewBox="0 0 400 220"><polygon points="0,0 400,0 400,215 0,140" fill="#ffffff"/></svg>
    <div class="brand-name"><span class="dot"></span>Wheelvale</div>
    <h2 class="why__title">Why choose us</h2>
    <ul class="bullets why__list">
      <li>Free delivery &amp; pickup at hotel</li>
      <li>No deposit</li>
      <li>Fast, reliable service</li>
      <li>Clean, ready-to-use equipment</li>
    </ul>
  </div>
</section>

<section class="panel panel--mobility">
  <div class="mobility__band"></div>
  <div class="mobility__sheet"></div>
  <div class="media scooter-photo" role="img" aria-label="Compact folding four-wheel mobility scooter with seat"></div>
  <h2 class="section-title mobility__title">Mobility</h2>
  <div class="rule mobility__rule"></div>
  <ul class="bullets mobility__list">
    <li>Lightweight</li>
    <li>Easy To Use</li>
    <li>Ideal For Sightseeing</li>
  </ul>
  <p class="mobility__copy">Meet our lightweight, ultra-compact dual battery mobility scooter for adults and seniors — easy to fold, carry and store in elevators, car boots and luggage spaces. Removable dual-battery system for good power and range. Not built for rough terrain, but perfect for smooth surfaces, trips, shopping or daily use. Weighing around 18 kg (without batteries), it’s easy to lift, manoeuvre and transport.</p>
</section>

</body>
</html>
```